Verdant Loop Advisors, LLC

I am looking for a simple, clear layout with my logo prominent and embossed, on the best quality card stock available. I would like the business name and phone number included on the card as well......I dont want my name anywhere on the card and I would like my logo embossed on the card......something simple with a white back......open to designs as long as they go along with recycling symbols and green type stuff.....The address, website, cell number, fax number, and email are listed below

4637 Pellham Brookside Road
Lindenmere, ST 10101

c. 555.555.3184 f. 555.555.6027
e. sales@verdantloopadvisors.example
w. www.verdantloopadvisors.example

Industry/Entity Type

Recycling

```html
<!DOCTYPE html>
<html lang="en">
<head>
<meta charset="utf-8">
<title>Verdant Loop Advisors, LLC – Business Card</title>
<link rel="stylesheet" href="https://fonts.googleapis.com/css2?family=Open+Sans:wght@400;600;800&display=swap">
<style>
  :root {
    --backdrop: #1c1c1c;
    --card-white: #ffffff;
    --card-dark-top: #4a4d51;
    --card-dark-bottom: #2e3033;
    --brand-green: #1f8a3c;
    --brand-ink: #2b2b22;
    --contact-text: #f2f2f2;
    --social-tile: #3f8fc2;
  }
  * { margin: 0; padding: 0; box-sizing: border-box; }
  html, body {
    width: 1200px;
    height: 638px;
    overflow: hidden;
    background: var(--backdrop);
    font-family: "Open Sans", Arial, sans-serif;
  }
  .stage {
    width: 1200px;
    height: 638px;
    display: flex;
    align-items: center;
    justify-content: center;
  }
  .business-card {
    width: 840px;
    height: 480px;
    display: flex;
    flex-direction: column;
    overflow: hidden;
  }
  .brand-band {
    height: 200px;
    background: var(--card-white);
    display: flex;
    align-items: center;
    padding-left: 120px;
    gap: 24px;
  }
  .brand-mark {
    width: 72px;
    height: 72px;
    background: var(--brand-green);
    flex: none;
  }
  .brand-name {
    font-weight: 800;
    font-size: 38px;
    line-height: 1.1;
    letter-spacing: 1px;
    color: var(--brand-ink);
    text-transform: uppercase;
  }
  .contact-panel {
    flex: 1;
    background: linear-gradient(180deg, var(--card-dark-top), var(--card-dark-bottom));
    color: var(--contact-text);
    padding: 40px 0 0 250px;
    font-size: 18px;
    line-height: 1.6;
  }
  .contact-panel .label { color: var(--brand-green); font-weight: 600; }
  .contact-panel .indent { padding-left: 24px; }
  .contact-panel .divider { margin: 0 10px; opacity: 0.7; }
  .social-row {
    display: flex;
    gap: 8px;
    margin: 18px 0 0 24px;
  }
  .social-tile {
    width: 28px;
    height: 28px;
    border-radius: 4px;
    background: var(--social-tile);
  }
</style>
</head>
<body>
<main class="stage">
  <section class="business-card" aria-label="Business card front">
    <header class="brand-band">
      <div class="brand-mark" aria-hidden="true"></div>
      <h1 class="brand-name">Verdant Loop<br>Advisors, LLC</h1>
    </header>
    <div class="contact-panel">
      <p class="address">4637 Pellham Brookside Road, Lindenmere, ST 10101</p>
      <p class="phones indent"><span class="label">c.</span> 555.555.3184<span class="divider">|</span><span class="label">f.</span> 555.555.6027</p>
      <p class="email indent"><span class="label">e.</span> sales@verdantloopadvisors.example</p>
      <p class="website">www.verdantloopadvisors.example</p>
      <div class="social-row" aria-hidden="true">
        <span class="social-tile"></span>
        <span class="social-tile"></span>
        <span class="social-tile"></span>
      </div>
    </div>
  </section>
</main>
</body>
</html>
```